LUXE Medical Spa

We'd like a business card with the reverse of the card for appointments. We like round corners and vertical design. We have a background image and bird logo to include with the following wording on the front:-
Luxe Medical Spa
248 Pemberton Street
NORTH BRAYFIELD
NB 5187
Phone 08 84391576
www.luxemedicalspa-example.com.au
Facebook luxemedicalspa
Instagram luxemedicalspa
On the back I'd like an appointment card layout please.
Cheers Dot

```html
<!DOCTYPE html>
<html lang="en">
<head>
<meta charset="utf-8">
<title>Luxe Medical Spa – Business &amp; Appointment Card</title>
<link rel="stylesheet" href="https://fonts.googleapis.com/css2?family=EB+Garamond:ital,wght@0,400;0,500;1,400&display=swap">
<style>
  :root {
    --mint: #a8d8bc;
    --paper: #ffffff;
    --ink: #1f1f1f;
    --swoosh-dark: #3a3a3c;
    --swoosh-light: #f2f2f2;
    --backdrop: #e6e6e6;
    --serif: "EB Garamond", Georgia, serif;
  }
  * { margin: 0; padding: 0; box-sizing: border-box; }
  html, body { width: 1200px; height: 838px; overflow: hidden; background: var(--backdrop); }
  .stage { position: relative; width: 1200px; height: 838px; }
  .card {
    position: absolute; top: 81px; width: 392px; height: 675px;
    border-radius: 27px; overflow: hidden; background: var(--paper);
    font-family: var(--serif); color: var(--ink);
  }
  .card--front { left: 155px; }
  .card--back { left: 644px; top: 83px; }
  .card__art { position: absolute; inset: 0; width: 392px; height: 675px; }
  .brand-name {
    position: absolute; left: 0; right: 0; text-align: center;
    color: var(--paper); font-weight: 400; letter-spacing: 0.18em; padding-left: 0.18em;
  }
  .card--front .brand-name { top: 155px; font-size: 50px; line-height: 60px; }
  .card--back .brand-name { top: 120px; font-size: 28px; }
  .centered { position: absolute; left: 0; right: 0; text-align: center; }
  .spa-name { top: 318px; font-size: 30px; font-weight: 500; }
  .address { top: 352px; font-size: 25px; line-height: 30px; font-style: normal; }
  .contacts { position: absolute; top: 458px; left: 99px; list-style: none; font-size: 24px; line-height: 30px; }
  .contacts li { display: flex; align-items: center; gap: 11px; }
  .contact-icon { width: 18px; height: 18px; flex: none; }
  .website { top: 614px; font-size: 23px; letter-spacing: 0.04em; }
  .appointment-title { top: 190px; font-size: 28px; font-weight: 400; letter-spacing: 0.2em; padding-left: 0.2em; }
  .appointment-fields { position: absolute; left: 34px; right: 40px; top: 324px; list-style: none; font-size: 25px; }
  .field { display: flex; align-items: baseline; height: 50px; }
  .field--for { height: 54px; }
  .field--blank { height: 45px; padding-left: 4px; }
  .field--blank::before { content: "\00a0"; }
  .field__line { flex: 1; border-bottom: 2px dotted var(--ink); margin-left: 6px; transform: translateY(-4px); }
  .cancel-note { top: 582px; font-size: 23px; font-style: italic; line-height: 28px; }
</style>
</head>
<body>
<main class="stage">

  <section class="card card--front" aria-label="Business card front">
    <svg class="card__art" viewBox="0 0 392 675" aria-hidden="true">
      <defs>
        <linearGradient id="swoosh-top" x1="0" x2="1" y1="0" y2="0">
          <stop offset="0" stop-color="var(--swoosh-dark)"/>
          <stop offset="1" stop-color="var(--swoosh-light)"/>
        </linearGradient>
        <linearGradient id="swoosh-bottom" x1="0" x2="1" y1="0" y2="0">
          <stop offset="0" stop-color="var(--swoosh-light)"/>
          <stop offset="1" stop-color="var(--swoosh-dark)"/>
        </linearGradient>
      </defs>
      <path d="M0,300 C160,296 300,262 392,180 V236 C300,292 160,306 0,307 Z" fill="url(#swoosh-top)"/>
      <path d="M0,0 H392 V180 C300,262 160,296 0,300 Z" fill="var(--mint)"/>
      <path d="M0,555 C110,546 180,560 240,580 C300,600 350,588 392,567 V580 C350,600 300,614 240,602 C180,590 110,582 0,587 Z" fill="url(#swoosh-bottom)"/>
      <path d="M0,587 C110,582 180,590 240,602 C300,614 350,600 392,580 V675 H0 Z" fill="var(--mint)"/>
    </svg>

    <h1 class="brand-name">LUXE</h1>

    <h2 class="centered spa-name">Luxe Medical Spa</h2>
    <address class="centered address">
      248 Pemberton Street<br>NORTH BRAYFIELD<br>NB 5187
    </address>

    <ul class="contacts">
      <li>
        <svg class="contact-icon" viewBox="0 0 18 18" aria-label="Phone" role="img">
          <rect width="18" height="18" rx="4" fill="var(--ink)"/>
          <path d="M4,7 Q9,3 14,7 L13,8.5 L11,7.5 L7,7.5 L5,8.5 Z M5.5,9 H12.5 L13,14 H5 Z" fill="var(--mint)"/>
        </svg>
        <span>08 84391576</span>
      </li>
      <li>
        <svg class="contact-icon" viewBox="0 0 18 18" aria-hidden="true"><rect width="18" height="18" rx="3" fill="var(--ink)"/></svg>
        <span>luxemedicalspa</span>
      </li>
      <li>
        <svg class="contact-icon" viewBox="0 0 18 18" aria-hidden="true"><rect x="1" y="1" width="16" height="16" rx="3" fill="none" stroke="var(--ink)" stroke-width="2"/></svg>
        <span>luxemedicalspa</span>
      </li>
    </ul>

    <p class="centered website">www.luxemedicalspa-example.com.au</p>
  </section>

  <section class="card card--back" aria-label="Appointment card back">
    <svg class="card__art" viewBox="0 0 392 675" aria-hidden="true">
      <defs>
        <linearGradient id="swoosh-top-back" x1="0" x2="1" y1="0" y2="0">
          <stop offset="0" stop-color="var(--swoosh-dark)"/>
          <stop offset="1" stop-color="var(--swoosh-light)"/>
        </linearGradient>
        <linearGradient id="swoosh-bottom-back" x1="0" x2="1" y1="0" y2="0">
          <stop offset="0" stop-color="var(--swoosh-light)"/>
          <stop offset="1" stop-color="var(--swoosh-dark)"/>
        </linearGradient>
      </defs>
      <path d="M0,298 C160,294 300,262 392,180 V236 C300,290 160,304 0,305 Z" fill="url(#swoosh-top-back)"/>
      <path d="M0,0 H392 V180 C300,262 160,294 0,298 Z" fill="var(--mint)"/>
      <path d="M0,529 C90,520 160,525 210,545 C270,568 330,562 392,541 V549 C330,578 270,588 210,572 C150,557 90,557 0,563 Z" fill="url(#swoosh-bottom-back)"/>
      <path d="M0,563 C90,557 150,557 210,572 C270,588 330,578 392,549 V675 H0 Z" fill="var(--mint)"/>
    </svg>

    <p class="brand-name">LUXE</p>
    <h2 class="centered appointment-title">APPOINTMENT</h2>

    <ul class="appointment-fields">
      <li class="field field--for"><span>For:</span><span class="field__line"></span></li>
      <li class="field field--blank"><span class="field__line"></span></li>
      <li class="field"><span>Date:</span><span class="field__line"></span></li>
      <li class="field"><span>Time:</span><span class="field__line"></span></li>
    </ul>

    <p class="centered cancel-note">If unable to keep the appointment,<br>please call</p>
  </section>

</main>
</body>
</html>
```